Business Card design for law firm = Brindlecourt Australia

We are seeking a new design for our business cards.
We are keeping our logo, which is attached.
We need space for
Name
Title
Address is , which is
Level 14
83 Tarrenby Street
Sydney NSW 2000
Phone :
Mobile :
Fax :
Email :
DX :
website www.brindlecourt.com.au

Industry/Entity Type

Law Firm / Banking and Finance

Contact Information for Business Card

We are seeking a new design for our business cards. We are keeping our logo. We need space for Name Title Address is Level 14 83 Tarrenby Street Sydney NSW 2000 Phone Mobile Fax Email DX website www.brindlecourt.com.au

Colors
0054AA
0677BA
7BADD7
CADEEF
E8F1F8

Requirements
Must have
• see our website for general feel www.brindlecourt.com.au

```html
<!DOCTYPE html>
<html lang="en">
<head>
<meta charset="utf-8">
<title>Brindlecourt Australia – Business Card</title>
<link rel="stylesheet" href="https://fonts.googleapis.com/css2?family=Montserrat:wght@400;500;700&display=swap">
<style>
  :root {
    --brand-deep: #0054AA;
    --brand-mid: #0677BA;
    --brand-soft: #7BADD7;
    --brand-pale: #CADEEF;
    --brand-mist: #E8F1F8;
    --ink-grey: #5a5f66;
    --card-white: #ffffff;
  }
  * { box-sizing: border-box; margin: 0; padding: 0; }
  html, body { width: 1200px; height: 1056px; overflow: hidden; }
  body {
    background: var(--brand-deep);
    font-family: "Montserrat", sans-serif;
    position: relative;
  }
  .card {
    position: absolute;
    left: 290px;
    width: 620px;
    height: 354px;
    background: var(--card-white);
    overflow: hidden;
  }
  .card--front { top: 120px; }
  .card--back  { top: 582px; }

  /* Front */
  .front-identity {
    position: absolute;
    left: 64px;
    top: 128px;
  }
  .front-name {
    font-size: 54px;
    font-weight: 500;
    line-height: 1;
    color: var(--brand-deep);
    letter-spacing: -0.5px;
  }
  .front-tagline {
    margin-top: 18px;
    font-size: 18px;
    font-weight: 400;
    letter-spacing: 2px;
    color: var(--brand-mid);
  }

  /* Back */
  .holder {
    position: absolute;
    left: 44px;
    top: 44px;
  }
  .holder-name {
    font-size: 28px;
    font-weight: 700;
    color: var(--brand-deep);
    letter-spacing: 0.5px;
  }
  .holder-title {
    margin-top: 4px;
    font-size: 15px;
    font-weight: 400;
    color: var(--ink-grey);
  }
  .holder-rule {
    margin-top: 8px;
    width: 108px;
    height: 3px;
    background: var(--brand-mid);
  }
  .address {
    position: absolute;
    left: 70px;
    top: 158px;
    font-size: 12.5px;
    font-style: normal;
    line-height: 1.4;
    color: var(--ink-grey);
  }
  .contacts {
    position: absolute;
    left: 70px;
    top: 212px;
    list-style: none;
    font-size: 12.5px;
    line-height: 1.45;
    color: var(--ink-grey);
  }
  .contacts li { display: flex; align-items: center; gap: 7px; }
  .contacts svg { width: 11px; height: 11px; fill: var(--brand-mid); flex: none; }

  .back-identity {
    position: absolute;
    right: 40px;
    bottom: 52px;
    text-align: right;
  }
  .back-name {
    font-size: 30px;
    font-weight: 500;
    color: var(--brand-deep);
    line-height: 1;
  }
  .back-tagline {
    margin-top: 8px;
    font-size: 10.5px;
    letter-spacing: 1px;
    color: var(--brand-mid);
  }
</style>
</head>
<body>

<section class="card card--front" aria-label="Business card front">
  <div class="front-identity">
    <div class="front-name">Brindlecourt</div>
    <div class="front-tagline">banking and finance lawyers</div>
  </div>
</section>

<section class="card card--back" aria-label="Business card back">
  <div class="holder">
    <div class="holder-name">MARA ELLISON</div>
    <div class="holder-title">Director / CEO</div>
    <div class="holder-rule"></div>
  </div>

  <address class="address">
    Level 14 83 Tarrenby Street<br>
    Sydney NSW 2000
  </address>

  <ul class="contacts">
    <li>
      <svg viewBox="0 0 12 12" aria-hidden="true"><path d="M1 4c0-2 2-3 5-3s5 1 5 3l-2 1-1-1H4L3 5zM3 6h6l1 5H2z"/></svg>
      +61-402-318-554
    </li>
    <li>
      <svg viewBox="0 0 12 12" aria-hidden="true"><path d="M2 1l2 0 1 3-1.5 1a7 7 0 0 0 3.5 3.5L8 7l3 1v2c0 1-1 1-1 1A9 9 0 0 1 1 2s0-1 1-1z"/></svg>
      +61-2-9186-4420
    </li>
    <li>
      <svg viewBox="0 0 12 12" aria-hidden="true"><path d="M3 1h5l1 1v2h1.5l.5 1v5H1V5l.5-1H3zM4 2v2h4V2zM3 7v2h6V7z"/></svg>
      +61-2-9186-4421
    </li>
    <li>
      <svg viewBox="0 0 12 12" aria-hidden="true"><path d="M0 2h12v8H0zM1 3l5 4 5-4v-.2H1z"/></svg>
      info@brindlecourt.com.au
    </li>
    <li>
      <svg viewBox="0 0 12 12" aria-hidden="true"><path d="M6 0a6 6 0 1 0 0 12A6 6 0 0 0 6 0zm0 1c.8 0 1.6 1.8 1.8 4H4.2C4.4 2.8 5.2 1 6 1zM1.1 5h2.1c.1-1.5.4-2.8.9-3.6A5 5 0 0 0 1.1 5zm7.7 0h2.1A5 5 0 0 0 7.9 1.4c.5.8.8 2.1.9 3.6zM1.1 7a5 5 0 0 0 3 3.6c-.5-.8-.8-2.1-.9-3.6zm3.1 0c.2 2.2 1 4 1.8 4s1.6-1.8 1.8-4zm4.6 0c-.1 1.5-.4 2.8-.9 3.6A5 5 0 0 0 10.9 7z"/></svg>
      www.brindlecourt.com.au
    </li>
  </ul>

  <div class="back-identity">
    <div class="back-name">Brindlecourt</div>
    <div class="back-tagline">banking and finance lawyers</div>
  </div>
</section>

</body>
</html>
```